Tidewell Outdoor Signage

We need an outdoor signage design for my company with new logo designed from makerhive. We do electrical, Air conditioning & Plumbing, installation, service, repairs and maintenance. The design shall be an eye catching that cannot miss ready it.

Industry/Entity Type

Electrical, Air conditioning, Plumbing

```html
<!DOCTYPE html>
<html lang="en">
<head>
<meta charset="utf-8">
<title>Tidewell Outdoor Signage</title>
<link href="https://fonts.googleapis.com/css2?family=Poppins:ital,wght@0,500;0,600;0,700;1,600&display=swap" rel="stylesheet">
<style>
  :root {
    --stage: #616161;
    --white: #ffffff;
    --orange: #f38e40;
    --red: #ec1f2a;
    --blue: #1a68ae;
    --ink: #3b3b3b;
    --mist: #ececec;
  }
  * { margin: 0; padding: 0; box-sizing: border-box; }
  html, body { width: 1200px; height: 1200px; overflow: hidden; background: var(--stage); font-family: "Poppins", sans-serif; }
  .sign { position: absolute; left: 200px; top: 400px; width: 800px; height: 400px; background: var(--white); overflow: hidden; }
  .backdrop-art { position: absolute; left: 0; top: 0; width: 800px; height: 330px; background: linear-gradient(160deg, rgba(236,236,236,0.9) 0%, rgba(255,255,255,0) 45%, rgba(236,236,236,0.6) 80%, rgba(255,255,255,0) 100%); }
  .stripe-orange { position: absolute; left: 0; top: 328px; width: 800px; height: 7px; background: var(--orange); }
  .band-blue { position: absolute; left: 0; top: 341px; width: 800px; height: 59px; background: var(--blue); }
  .hero-mark { position: absolute; left: 19px; top: 50px; width: 409px; height: 320px; border-radius: 160px 40px 160px 160px; background: linear-gradient(135deg, var(--orange) 0%, var(--red) 50%, var(--blue) 100%); border: 6px solid var(--white); }
  .brand { position: absolute; left: 575px; top: 120px; width: 215px; text-align: center; }
  .brand-name { font-weight: 600; font-size: 46px; line-height: 1; color: var(--orange); letter-spacing: -0.5px; }
  .brand-services { margin-top: 6px; font-weight: 600; font-size: 10px; display: flex; justify-content: space-between; }
  .svc-electrical { color: var(--red); }
  .svc-air { color: var(--blue); }
  .svc-plumbing { color: var(--orange); }
  .contact-label { position: absolute; left: 460px; top: 221px; font-weight: 600; font-style: italic; font-size: 20px; color: var(--ink); }
  .pill { position: absolute; right: 0; height: 38px; background: var(--red); border-radius: 19px 0 0 19px; display: flex; align-items: center; color: var(--white); font-weight: 600; }
  .pill-phone { left: 607px; top: 215px; font-size: 18px; }
  .pill-email { left: 450px; top: 271px; font-size: 16.5px; }
  .pill-icon { width: 26px; height: 26px; margin-left: 7px; border-radius: 50%; background: var(--white); display: flex; align-items: center; justify-content: center; flex: none; }
  .pill-phone .pill-text { margin-left: 24px; letter-spacing: 0.5px; }
  .pill-email .pill-text { margin-left: 24px; }
  .web { position: absolute; left: 413px; top: 355px; display: flex; align-items: center; color: var(--white); font-weight: 600; font-size: 21px; }
  .web-text { margin-left: 15px; }
</style>
</head>
<body>
  <main class="sign">
    <div class="backdrop-art" role="img" aria-label="Faint grey decoration of a tap, lightning bolt and water swirl"></div>
    <div class="stripe-orange"></div>
    <div class="band-blue"></div>
    <div class="hero-mark" role="img" aria-label="Large brand emblem in orange, red and blue"></div>

    <div class="brand">
      <div class="brand-name">Tidewell</div>
      <div class="brand-services">
        <span class="svc-electrical">Electrical</span>
        <span class="svc-air">Air Conditioning</span>
        <span class="svc-plumbing">Plumbing</span>
      </div>
    </div>

    <div class="contact-label">CONTACT US:</div>

    <div class="pill pill-phone">
      <span class="pill-icon">
        <svg width="14" height="14" viewBox="0 0 24 24"><path fill="#ec1f2a" d="M6.6 10.8a15.1 15.1 0 0 0 6.6 6.6l2.2-2.2a1 1 0 0 1 1-.25 11.4 11.4 0 0 0 3.6.57 1 1 0 0 1 1 1V20a1 1 0 0 1-1 1A17 17 0 0 1 3 4a1 1 0 0 1 1-1h3.5a1 1 0 0 1 1 1c0 1.25.2 2.45.57 3.57a1 1 0 0 1-.25 1z"/></svg>
      </span>
      <span class="pill-text">0400 555 017</span>
    </div>

    <div class="pill pill-email">
      <span class="pill-icon">
        <svg width="15" height="11" viewBox="0 0 15 11"><rect x="0.75" y="0.75" width="13.5" height="9.5" fill="none" stroke="#ec1f2a" stroke-width="1.5"/><path d="M0.75 0.75 7.5 6 14.25 0.75M0.75 10.25 5.5 5M14.25 10.25 9.5 5" fill="none" stroke="#ec1f2a" stroke-width="1.2"/></svg>
      </span>
      <span class="pill-text">info@tidewellelectrical.com.au</span>
    </div>

    <div class="web">
      <svg width="29" height="29" viewBox="0 0 30 30"><circle cx="15" cy="15" r="13" fill="none" stroke="#fff" stroke-width="2.5"/><ellipse cx="15" cy="15" rx="6" ry="13" fill="none" stroke="#fff" stroke-width="2.5"/><path d="M2 15h26M4 8.5h22M4 21.5h22" stroke="#fff" stroke-width="2.5"/></svg>
      <span class="web-text">www.tidewellelectrical.com.au</span>
    </div>
  </main>
</body>
</html>
```